Einzelne Suchwerk Landingpage
Suchwerk Landingpage für das Thema
„Vergleich von Private Rentenversicherungen“
Haupt Suchbegriffe für die die Landingpage verwendet werden soll:
-Private Rente
-Vergleich Private Rente
-Private Rentenversicherung
Mitbewerber:
Siehe Suchwerk Ergebnisse bei Eingabe obiger Suchbegriffe
Zielgruppe:
Alle Bundesbürger die sich mit privater Altersvorsorge beschäftigen.
Verstärkt Männer aber auch Frauen im Alter zwischen ca. 35-55 J.
Designanforderungen:
Spagat zwischen
Priorität I: ansprechenden des Besuchers auf emotionaler Ebene (Einbindung von Menschenbildern, etc.)
und
Priorität II: Ausdruck von Seriosität, Kompetenz und Unabhängigkeit
Als Beispiel-Designvorlagen von Mitbewerbern finde ich folgende Seite sehr ansprechend:
https://www1.ruhestand-kassenblick.de/ (hier ist mir nur das Formular zu groß, zu wenig Platz für Text)
Oder
http://www.geldlotse17.info/Sofortrente-Vergleich/index.html
(Design ist nicht so toll, aber klar strukturiert)
Vorlage für die Strukturierung der Seite:
Gute Erfahrungen was die Conversionsraten angeht habe ich mit der aktuell schon bestehenden Seite zum Thema „Rürup Rente“ gemacht.
www.kassenblick-basisplan-neu.de
Sicher ist diese was das Design angeht optimierungsfähig.
Was das Verhältnis Text/Formular angeht finde ich den Aufbau jedoch ganz gut bzw. hat sich die Seite bewährt. Die Unterseiten für Datenschutz und Impressum können ebenfalls übernommen werden.
Content
Der Text für die Seite ist hier hinterlegt:
www.wandoret.com/Inhalt_Text.docx
Formular:
Für das Formular könnten Sie ggf. auch den Quelltext der bestehenden Rürup Seite (s.o.) nutzen.
Das müsste dann nur minimal abgeändert werden.
www.wandoret.com/Formular.docx
Bei weiteren Rückfragen stehe ich gerne zur Verfügung.

```html
<!DOCTYPE html>
<html lang="de">
<head>
<meta charset="utf-8">
<title>Private Renten im Vergleich</title>
<link rel="stylesheet" href="https://fonts.googleapis.com/css2?family=Arimo:wght@400;700&family=Gelasio:wght@700&family=Ubuntu:wght@500;700&display=swap">
<style>
  :root{
    --ink:#111;
    --navy:#124e80;
    --header:#222;
    --gold:#f3c232;
    --orange:#e8740c;
    --green:#6bae1c;
    --tick:#1aa31a;
    --panel:#e4eef8;
    --field-border:#a9b7c6;
    --muted:#444;
  }
  *{box-sizing:border-box;margin:0;padding:0}
  html,body{width:983px;height:1200px;overflow:hidden;background:#fff}
  body{position:relative;font-family:"Arimo",Arial,sans-serif;color:var(--ink);font-size:12px}
  .site-header{position:absolute;left:0;top:0;width:983px;height:57px;background:var(--header)}
  .site-name{position:absolute;left:37px;top:8px;font-family:"Ubuntu",sans-serif;font-weight:700;font-size:32px;color:var(--gold);letter-spacing:.2px}
  .breadcrumb{position:absolute;left:37px;top:66px;font-weight:700;font-size:12px;color:var(--muted)}
  .page-title{position:absolute;left:37px;top:86px;font-family:"Gelasio",Georgia,serif;font-size:25px;color:var(--navy)}
  .hero-couple{position:absolute;left:37px;top:133px;width:239px;height:189px;background:linear-gradient(135deg,#d9d3c8,#c9a78c 55%,#f1ece4)}
  .hero-bench{position:absolute;left:277px;top:133px;width:478px;height:189px;background:linear-gradient(180deg,#4f7fb8 0%,#9fc0de 48%,#5b6c3c 70%,#3d5a24 100%)}
  .deadline-banner{position:absolute;left:592px;top:140px;width:340px;height:126px;transform:rotate(-4deg);background:linear-gradient(180deg,#f6a30f,#ec5f06);box-shadow:3px 4px 6px rgba(0,0,0,.35);color:#fff;font-family:"Ubuntu",sans-serif;font-weight:700;font-size:19px;line-height:24px;text-align:center;padding-top:18px}
  .content{position:absolute;left:37px;width:575px}
  .intro{top:345px;font-weight:700;font-size:14.5px;line-height:18px;color:var(--navy)}
  .pitch{top:430px;font-size:13px;line-height:16px;color:var(--orange)}
  .pitch strong{font-weight:700}
  .section-title{font-weight:700;font-size:16px;color:var(--navy);margin-bottom:3px}
  .content p{font-size:12px;line-height:14.5px}
  .ticks{list-style:none;margin-top:10px}
  .ticks li{position:relative;padding-left:36px;font-size:12px;line-height:14.7px}
  .ticks li svg{position:absolute;left:12px;top:1px}
  .ticks li.plain{padding-left:36px}
  .offer-kicker{position:absolute;left:629px;top:346px;font-size:14px;color:#1d3c5a}
  .offer-title{position:absolute;left:629px;top:367px;font-weight:700;font-size:18.5px;color:var(--green)}
  .offer-note{position:absolute;left:632px;top:392px;font-size:12px;line-height:14px;color:#1d3c5a}
  .offer-note em{font-style:normal;color:var(--green)}
  .request-form{position:absolute;left:628px;top:428px;width:341px;height:518px;background:var(--panel)}
  .row{position:absolute;left:0;width:341px;height:24px}
  .row label{position:absolute;right:178px;top:4px;font-size:12px;color:#222;white-space:nowrap}
  .field{position:absolute;top:0;height:24px;background:#fff;border:1px solid var(--field-border)}
  .select{position:absolute;top:2px;height:19px;border:1px solid #8d9bb0;border-radius:4px;background:linear-gradient(#fbfdff,#d9e3ef);font-size:11px;line-height:17px;text-align:center;padding-right:16px;color:#222}
  .select::after{content:"";position:absolute;right:0;top:0;width:14px;height:17px;border-radius:0 3px 3px 0;background:linear-gradient(#6fa6ea,#2c6fd0)}
  .privacy{position:absolute;left:34px;top:427px;font-size:11px;line-height:14px;color:#222}
  .consent{position:absolute;left:32px;top:466px;font-size:11px;color:#222;display:flex;align-items:center;gap:6px}
  .consent .box{width:14px;height:14px;border:1px solid #999;border-radius:3px;background:#fff}
  .consent a{color:#1a5fd0}
  .lock{position:absolute;left:264px;top:425px}
  .submit{position:absolute;left:51px;top:500px;width:256px;height:46px;border-radius:3px;background:linear-gradient(#86c433,#5a9c16);box-shadow:0 2px 3px rgba(0,0,0,.3);color:#fff;font-weight:700;font-size:18px;text-align:center;line-height:46px}
  .seal{position:absolute;left:869px;top:958px}
  .next-steps{position:absolute;left:625px;top:1056px;width:345px;font-size:11px;line-height:13.4px;color:#111}
  .site-footer{position:absolute;left:0;top:1170px;width:983px;height:30px;background:var(--header);color:#fff;font-weight:700;font-size:14px;padding:5px 0 0 35px}
</style>
</head>
<body>
<header class="site-header"><div class="site-name">www.rentenblick-vergleich.com</div></header>

<div class="breadcrumb">Altersvorsorge / Private Rentenversicherungen:</div>
<h1 class="page-title">Welche Private Rentenversicherung nehmen?</h1>

<div class="hero-couple" role="img" aria-label="Foto eines lächelnden älteren Paares"></div>
<div class="hero-bench" role="img" aria-label="Foto von vier Senioren auf einer Bank am Meer"></div>
<div class="deadline-banner">ACHTUNG!!<br>Bis 31.12.2011 noch höhere<br>Garantieverzinsung<br>für die gesamte Laufzeit sichern!!!</div>

<div class="content intro">Bevor Sie sich für die Private Rentenversicherung eines bestimmten Anbieters entscheiden, sollten Sie wissen, was vergleichbare Rentenversicherungen leisten. Welcher Anbieter für Sie attraktiv ist, kann nämlich je nach Eintrittsalter, Geschlecht oder Anlagementalität sehr variieren.</div>

<div class="content pitch">Der Vergleich lohnt sich für Sie, denn gerade bei <strong>Privaten Rentenversicherungen</strong> gibt es riesige Unterschiede. Selbst wenn Ihnen die Differenz bei den Rentenergebnissen der Anbieter eher klein erscheint,können sich über die gesamte Rentenphase Unterschiede von <strong>10.000 EUR</strong> und mehr ergeben.</div>

<section class="content" style="top:518px">
  <h2 class="section-title">Als unabhängige Vorsorgespezialisten holen wir mehr für Sie heraus!</h2>
  <p>Fordern Sie jetzt Ihren kostenlosen und unverbindlichen Marktvergleich an.<br>Unser Marktvergleich bietet mehr…</p>
  <ul class="ticks" style="margin-top:16px">
    <li><svg width="17" height="13" viewBox="0 0 17 13"><path d="M1 7l5 5L16 1" fill="none" stroke="#1aa31a" stroke-width="3.2"/></svg>Vergleich von über 45 Versicherungen</li>
    <li><svg width="17" height="13" viewBox="0 0 17 13"><path d="M1 7l5 5L16 1" fill="none" stroke="#1aa31a" stroke-width="3.2"/></svg>Klassische- und Fondsprodukte</li>
    <li><svg width="17" height="13" viewBox="0 0 17 13"><path d="M1 7l5 5L16 1" fill="none" stroke="#1aa31a" stroke-width="3.2"/></svg>Inkl. Direktversicherer</li>
    <li><svg width="17" height="13" viewBox="0 0 17 13"><path d="M1 7l5 5L16 1" fill="none" stroke="#1aa31a" stroke-width="3.2"/></svg>Inkl. berufsspezifischer Sonderrabatttarife</li>
    <li><svg width="17" height="13" viewBox="0 0 17 13"><path d="M1 7l5 5L16 1" fill="none" stroke="#1aa31a" stroke-width="3.2"/></svg>Tarife mit vergünstigten Kosten</li>
  </ul>
</section>

<section class="content" style="top:671px">
  <h2 class="section-title">Das gesetzliche Rentenniveau genügt nicht zur Grundversorgung!</h2>
  <p style="margin-top:12px">Mittlerweile ist es fast jedem klar. Die gesetzliche Rente wird nicht zur Grundversorgung ausreichen.<br>Daher ist private Vorsorge unausweichlich.<br>Jedoch unterschätzen die meisten Bundesbürger die Höhe der Rentenlücke im Alter.</p>
</section>

<section class="content" style="top:764px">
  <h2 class="section-title">Folgende Faktoren werden meist unterschätzt:</h2>
  <ul class="ticks" style="margin-top:13px">
    <li><svg width="17" height="13" viewBox="0 0 17 13"><path d="M1 7l5 5L16 1" fill="none" stroke="#1aa31a" stroke-width="3.2"/></svg>Hohe Inflation</li>
    <li><svg width="17" height="13" viewBox="0 0 17 13"><path d="M1 7l5 5L16 1" fill="none" stroke="#1aa31a" stroke-width="3.2"/></svg>Immer weiter steigende Sozialabgaben</li>
    <li><svg width="17" height="13" viewBox="0 0 17 13"><path d="M1 7l5 5L16 1" fill="none" stroke="#1aa31a" stroke-width="3.2"/></svg>Insbesondere Krankenversicherungsausgaben</li>
    <li><svg width="17" height="13" viewBox="0 0 17 13"><path d="M1 7l5 5L16 1" fill="none" stroke="#1aa31a" stroke-width="3.2"/></svg>Steigende Lebenshaltungskosten</li>
    <li><svg width="17" height="13" viewBox="0 0 17 13"><path d="M1 7l5 5L16 1" fill="none" stroke="#1aa31a" stroke-width="3.2"/></svg>Pflegekosten</li>
    <li class="plain">etc.</li>
  </ul>
</section>

<section class="content" style="top:914px">
  <h2 class="section-title">Die Vorteile der privaten Rentenversicherung:</h2>
  <ul class="ticks" style="margin-top:13px">
    <li><svg width="17" height="13" viewBox="0 0 17 13"><path d="M1 7l5 5L16 1" fill="none" stroke="#1aa31a" stroke-width="3.2"/></svg>Maximale Flexibilität</li>
    <li><svg width="17" height="13" viewBox="0 0 17 13"><path d="M1 7l5 5L16 1" fill="none" stroke="#1aa31a" stroke-width="3.2"/></svg>Beliebige Vererbbarkeit</li>
    <li><svg width="17" height="13" viewBox="0 0 17 13"><path d="M1 7l5 5L16 1" fill="none" stroke="#1aa31a" stroke-width="3.2"/></svg>Wahlrecht Kapital oder Rente</li>
    <li><svg width="17" height="13" viewBox="0 0 17 13"><path d="M1 7l5 5L16 1" fill="none" stroke="#1aa31a" stroke-width="3.2"/></svg>Garantierte lebenslange Rente</li>
    <li><svg width="17" height="13" viewBox="0 0 17 13"><path d="M1 7l5 5L16 1" fill="none" stroke="#1aa31a" stroke-width="3.2"/></svg>Abgeltungssteuerfrei sparen</li>
    <li><svg width="17" height="13" viewBox="0 0 17 13"><path d="M1 7l5 5L16 1" fill="none" stroke="#1aa31a" stroke-width="3.2"/></svg>Attraktive Rendite mit Garantieverzinsung</li>
  </ul>
</section>

<div class="offer-kicker">Private Rente: Anbieter &amp; Tarife</div>
<div class="offer-title">Private Renten im Vergleich</div>
<div class="offer-note">Fordern Sie hier Ihren <em>kostenlosen</em><br>Versicherungsvergleich an.</div>

<form class="request-form">
  <div class="row" style="top:22px"><label>Anlagebetrag (€ / Zahlart ) :</label><span class="field" style="left:169px;width:79px"></span><span class="select" style="left:255px;width:79px">Monatlich</span></div>
  <div class="row" style="top:53px"><label style="right:108px">Rentenauszahlung : im Alter von</label><span class="field" style="left:235px;width:57px"></span><label style="right:8px">Jahren</label></div>
  <div class="row" style="top:85px"><label>Bruttoeinkommen (€/ Jahr ):</label><span class="field" style="left:169px;width:165px"></span></div>
  <div class="row" style="top:112px"><label>Kinder:</label><span class="select" style="left:169px;width:165px">Bitte auswaehlen</span></div>
  <div class="row" style="top:139px"><label>Familienstand:</label><span class="select" style="left:169px;width:165px">Bitte auswaehlen</span></div>
  <div class="row" style="top:164px"><label>Beruf, Berufstand:</label><span class="field" style="left:169px;width:65px"></span><span class="select" style="left:240px;width:94px">Angestellter</span></div>
  <div class="row" style="top:192px"><label>Geburtsdatum:</label><span class="select" style="left:177px;width:43px">1</span><span class="select" style="left:224px;width:56px">Monat</span><span class="select" style="left:284px;width:50px">Jahr</span></div>
  <div class="row" style="top:219px"><label>Anrede, Vorname, Name:</label><span class="select" style="left:169px;width:46px">Frau</span><span class="field" style="left:218px;width:59px"></span><span class="field" style="left:280px;width:54px"></span></div>
  <div class="row" style="top:251px"><label>Strasse, Hausnummer:</label><span class="field" style="left:169px;width:165px"></span></div>
  <div class="row" style="top:280px"><label>PLZ, Wohnort:</label><span class="field" style="left:169px;width:60px"></span><span class="field" style="left:232px;width:102px"></span></div>
  <div class="row" style="top:309px"><label>Tel.-Nr. / Erreichbarkeit:</label><span class="field" style="left:169px;width:60px"></span><span class="select" style="left:239px;width:95px">Ganztags</span></div>
  <div class="row" style="top:338px"><label>eMail-Adresse:</label><span class="field" style="left:169px;width:165px"></span></div>

  <div class="privacy">Sicherheit &amp; Datenschutz<br>Ihre Daten sind sicher und geschuetzt.</div>
  <svg class="lock" width="26" height="34" viewBox="0 0 26 34" aria-hidden="true"><path d="M6 15V10a7 7 0 0 1 14 0v5" fill="none" stroke="#777" stroke-width="3"/><rect x="2" y="14" width="22" height="18" rx="2" fill="#e8b820"/><rect x="11.5" y="20" width="3" height="7" fill="#5a4300"/></svg>
  <div class="consent"><span class="box"></span>Ich habe den <a>Datenschutz</a> gelesen und akzeptiert.</div>
  <div class="submit">Kostenfreier Vergleich</div>
</form>

<svg class="seal" width="106" height="102" viewBox="0 0 106 102" role="img" aria-label="Prüfsiegel"><circle cx="53" cy="50" r="46" fill="none" stroke="#1a4f9c" stroke-width="8"/><circle cx="53" cy="50" r="30" fill="#e6eef8"/></svg>

<div class="next-steps">Sie haben Ihre Angaben gemacht. So geht es weiter:<br>In Kürze erhalten Sie Ihren Versicherungsvergleich.<br>Der Vergleich wird softwaregestützt von unseren qualifizierten Spezialisten erstellt.Dieser Service ist kostenfrei. Wir bitten Sie nur ernsthafte und vollständige Angaben zu machen, da ansonsten kein Vergleich erstellt werden kann. Bei weiteren Fragen stehen Ihnen unsere Experten via Onlineberatung zur Verfügung.</div>

<footer class="site-footer">Kontakt &nbsp;- Impressum</footer>
</body>
</html>
```